Proverbs Sermon Series Artwork

We are in need of new artwork for an upcoming sermon series that our Senior Pastor will be preaching for at least the next 6 months. This graphic will be used extensively on our app, website, and in worship services and needs to be of excellent quality and also provide meaning behind the entirety of the series. Proverbs is a very rich book of the Bible that deals with wisdom and how to live according to God's principles. The graphic needs to reflect this truth and communicate to those who see it that there are different ways that each of us can choose to live.
We are very flexible on the goal of this piece and don't really have anything in mind. The graphic that is the most professional but also communicated the goal of the sermon series will be the one selected. Please see the must haves to get an idea of different formats we would like to use this graphic in. It will be a key image in the life of our church over the next 6-12 months.
Thanks for looking into this project. I hope you will submit a graphic design and use your God given talents to help us (and make a little money on the side). ArtFolio has served us well in the past and we are excited to use it again.
Updates
As of right now, I have 3 good designs from 2 designers. I would love to see the edits made based on feedback provided. I think there is a lot of potential in all 3 designs. If you have questions please let me know. After all artwork is submitted I will be presenting it to the senior pastor and he will select the one he likes the best. I would like to bring him 5 designs so there is still room for some other good submissions from new designers! Also, I uploaded a road sign image. I would like to see something with an image like that from someone.
Target Market(s)
Church members, app users, website visitors
Industry/Entity Type
Religious
Requirements
Must have
- Artwork must include Proverbs in a bold easy to read font. The graphic must also lend itself to different formats. 1920x1080 wide format graphic, 1024x1024 square icon, 1920x692 banner.
Nice to have
- The sermon series is about us having choices on how to live our lives and the goal that we should take God's way instead of ours. This would lend itself well to road signs or maybe something cool with nature. Maybe even a word art as proverbs is a lot of sayings that speak to wisdom of the Christian walk. I'm pretty flexible.
Should not have
- Not overly feminine like most church artwork. This is geared to the whole body, not women.

```html
<!DOCTYPE html>
<html lang="en">
<head>
<meta charset="utf-8">
<title>Proverbs — Two Ways to Live</title>
<link rel="stylesheet" href="https://fonts.googleapis.com/css2?family=Montserrat:wght@300;700;900&display=swap">
<style>
  :root {
    --thorn-dark: #4f4136;
    --thorn-mid: #8a7766;
    --thorn-light: #b7a592;
    --leaf-deep: #2f8a1e;
    --leaf-mid: #5fb82f;
    --leaf-bright: #a6d93a;
    --white: #ffffff;
    --accent-green: #8dc63f;
  }
  html, body {
    margin: 0;
    padding: 0;
    overflow: hidden;
    background: #ffffff;
  }
  .series-art {
    position: relative;
    width: 1200px;
    height: 675px;
    overflow: hidden;
    font-family: "Montserrat", sans-serif;
  }
  .backdrop {
    position: absolute;
    inset: 0;
    width: 1200px;
    height: 675px;
    display: block;
  }
  .series-title {
    position: absolute;
    left: 112px;
    top: 178px;
    margin: 0;
    display: flex;
    align-items: baseline;
    color: var(--white);
    font-size: 162px;
    line-height: 1;
    white-space: nowrap;
  }
  .title-bold {
    font-weight: 900;
    letter-spacing: -3px;
  }
  .title-light {
    font-weight: 300;
    letter-spacing: 14px;
    margin-left: 8px;
  }
  .series-tagline {
    position: absolute;
    left: 594px;
    top: 362px;
    width: 499px;
    height: 62px;
    margin: 0;
    background: var(--white);
    color: var(--accent-green);
    font-weight: 700;
    font-size: 43px;
    line-height: 62px;
    text-align: center;
    letter-spacing: -0.5px;
    white-space: nowrap;
  }
</style>
</head>
<body>
  <main class="series-art">
    <svg class="backdrop" viewBox="0 0 1200 675" xmlns="http://www.w3.org/2000/svg">
      <defs>
        <linearGradient id="thornTone" x1="0" y1="0" x2="1" y2="1">
          <stop offset="0" stop-color="var(--thorn-light)"/>
          <stop offset="0.5" stop-color="var(--thorn-mid)"/>
          <stop offset="1" stop-color="var(--thorn-dark)"/>
        </linearGradient>
        <radialGradient id="leafTone" cx="0.8" cy="0.3" r="0.9">
          <stop offset="0" stop-color="var(--leaf-bright)"/>
          <stop offset="0.55" stop-color="var(--leaf-mid)"/>
          <stop offset="1" stop-color="var(--leaf-deep)"/>
        </radialGradient>
      </defs>
      <rect class="leaf-photo" role="img" aria-label="Photograph of fresh green leaves on a branch in soft sunlight" x="0" y="0" width="1200" height="675" fill="url(#leafTone)"/>
      <polygon class="thorn-photo" role="img" aria-label="Sepia-toned photograph of tangled thorny branches" points="0,0 704,0 444,675 0,675" fill="url(#thornTone)"/>
    </svg>

    <h1 class="series-title">
      <span class="title-bold">PROV</span><span class="title-light">ERBS</span>
    </h1>
    <p class="series-tagline">TWO WAYS TO LIVE</p>
  </main>
</body>
</html>
```